Real Estate Design Website

I would like to have a design for "real estate agent" website. It needs to be in a "Responsive" framework.

The design need to be suitable for different viewer from all around the world. It needs to be modern. It'd be great if there is a design for mobile and tovix/tablet (it's all under responsive framework). It needs to be easy to navigate and look modern

Target Market(s)

End user/Real estate buyers from different part of the world

Industry/Entity Type

Real Estate

Requirements
Must have
• It's for real estate agent website which is used to represent their brand/image but at the same time it also for their client which is real estate buyers
Should not have
• Should not be boring design/out of date

```html
<!DOCTYPE html>
<html lang="en">
<head>
<meta charset="utf-8">
<title>Havenmark Homes</title>
<link href="https://fonts.googleapis.com/css2?family=Oswald:wght@400;500&family=PT+Serif&family=Arimo:ital,wght@0,400;0,700;1,400;1,700&family=Open+Sans:wght@400;600&display=swap" rel="stylesheet">
<style>
:root{
  --cyan:#19b4f0;
  --blue:#11a3ee;
  --blue-deep:#0a8fd8;
  --ink:#111;
  --dark:#1b1b1b;
  --grey:#e7e7e7;
  --text:#555;
  --fb:#3a5c9e;
  --tw:#22b6ee;
  --li:#2a8fc4;
}
*{box-sizing:border-box;margin:0;padding:0}
html,body{width:1155px;height:1200px;overflow:hidden;background:#fff}
.page{position:absolute;left:0;top:0;width:1400px;height:1454px;transform:scale(.825);transform-origin:0 0;font-family:Arimo,Arial,sans-serif;color:var(--text)}
.abs{position:absolute}
.cond{font-family:Oswald,"Arial Narrow",sans-serif;font-weight:400;text-transform:uppercase}

/* header */
.header{left:0;top:0;width:1400px;height:104px;background:#fff}
.brand{left:242px;top:30px;display:flex;align-items:center;gap:12px}
.brand-mark{width:30px;height:30px;background:var(--cyan)}
.brand-name{font-family:Oswald,"Arial Narrow",sans-serif;font-weight:500;font-size:40px;line-height:48px;color:var(--ink);text-transform:uppercase}
.lang-label{left:910px;top:38px;color:var(--cyan);font-size:17px;letter-spacing:-.3px}
.lang-select{left:1068px;top:37px;width:86px;height:23px;background:var(--cyan);border-radius:4px;color:#fff;font-size:12px;line-height:23px;padding-left:14px}
.lang-select svg{position:absolute;right:11px;top:8px}

/* nav */
.nav{left:0;top:104px;width:1400px;height:48px;background:linear-gradient(#363636,#262626)}
.nav-item{top:0;height:48px;line-height:48px;color:#fff;font-size:20px}
.nav-item.active{background:#1e1e1e;color:var(--cyan);padding:0 20px}
.social-dot{top:80px;width:48px;height:48px;border-radius:50%;background:radial-gradient(circle at 50% 40%,#444,#1e1e1e);border:3px solid #2f2f2f;box-shadow:0 2px 3px rgba(0,0,0,.5)}

/* hero */
.hero-dark{left:0;top:152px;width:1400px;height:379px;background:linear-gradient(120deg,#565656,#3a3a3a 45%,#4a4a4a)}
.hero-blue{left:0;top:531px;width:1400px;height:219px;background:var(--blue)}
.photo-frame{left:215px;top:164px;width:656px;height:420px;background:#0d0d0d}
.photo{left:5px;top:6px;width:645px;height:407px;background:linear-gradient(100deg,#3a4a78 0%,#2c3f6a 16%,#6d6a62 30%,#8b8478 55%,#b9b2a6 75%,#d9d6cf 100%)}
.search{left:881px;top:164px;width:314px;height:420px;background:var(--dark)}
.search-title{left:22px;top:12px;color:var(--cyan);font-size:21px;letter-spacing:-.3px}
.field-label{left:24px;color:#aaa;font-size:13px;letter-spacing:.5px}
.select{height:28px;background:#2a2a2a;border:1px solid #333;color:#777;font-style:italic;font-size:12px;line-height:26px;padding-left:9px}
.select::after{content:"";position:absolute;right:2px;top:2px;width:16px;height:22px;background:#555}
.select svg{position:absolute;right:6px;top:10px;z-index:1}
.toggle-rent{left:136px;top:130px;color:var(--cyan);font-size:20px}
.toggle-sale{left:184px;top:131px;width:79px;height:30px;background:var(--cyan);color:#111;font-size:20px;text-align:center;line-height:29px}
.slider{left:26px;top:279px;width:254px;height:34px;border-radius:17px;background:#3a3a3a;box-shadow:inset 0 2px 4px #000}
.slider-track{left:24px;top:15px;width:208px;height:3px;background:#7ab7f0}
.knob{top:9px;width:15px;height:15px;border-radius:50%;background:#eee}
.scale-lbl{top:322px;font-size:9px;color:#ccc}
.find-btn{left:48px;top:366px;width:202px;height:34px;background:linear-gradient(#4a4a4a,#2c2c2c);border:1px solid #555;border-radius:3px;color:var(--cyan);font-family:"PT Serif",serif;font-size:12px;text-align:center;line-height:32px}

/* categories */
.cat-icon{top:604px;width:136px;height:136px;border-radius:50%;background:#f1f1f1;border:4px solid #d9d9d9}
.cat-icon span{position:absolute;left:30px;top:26px;width:68px;height:76px;border-radius:8px}
.cat-kicker{top:619px;color:#fff;font-size:19px;letter-spacing:1px}
.cat-word{top:641px;font-family:"PT Serif",Georgia,serif;font-size:64px;line-height:70px;color:#111;transform:scaleX(.74);transform-origin:0 0;white-space:nowrap}

/* featured */
.divider{left:0;top:750px;width:1400px;height:10px;background:#333}
.featured{left:0;top:760px;width:1400px;height:142px;background:linear-gradient(#fff,#ebebeb);border-bottom:1px solid #ddd}
.featured-title{left:0;top:8px;width:1400px;text-align:center;color:#222;font-size:27px}
.thumb{top:54px;width:123px;height:70px;border:3px solid #ccc}

/* blog */
.blog-kicker{left:232px;top:936px;font-family:Oswald,sans-serif;font-style:italic;color:#999;font-size:28px;font-weight:400}
.blog-title{left:395px;top:934px;color:#222;font-size:28px}
.blog-photo{left:230px;top:997px;width:233px;height:147px;background:#ddd;padding:6px}
.blog-photo div{width:221px;height:135px;background:linear-gradient(#7e8a99,#a8a39c 55%,#6a4a3a)}
.meta{top:1005px;font-size:13px;font-style:italic;color:#222}
.meta b{color:var(--blue-deep)}
.blog-date{left:750px;top:1005px;font-size:13px;font-style:italic;color:#aaa}
.blog-body{left:477px;top:1032px;width:370px;font-size:12px;line-height:18.5px;color:#555}
.more{left:477px;top:1130px;color:var(--blue-deep);font-weight:700;font-size:13px}

.side{left:875px;top:922px;width:320px;height:310px;background:var(--grey)}
.side-head{left:10px;top:6px;width:300px;height:68px;background:linear-gradient(#fbfbfb,#eee);font-size:28px;color:#222;padding:8px 20px}
.post{left:10px;width:300px;height:73px;background:#fff;border-top:1px solid #ddd;font-family:"Open Sans",sans-serif}
.post svg{position:absolute;left:16px;top:20px}
.post-text{left:40px;top:17px;font-size:13.5px;color:#333}
.post-by{left:40px;top:43px;font-size:10.5px;color:#aaa;font-style:italic}
.post-by b{color:var(--blue-deep);font-weight:400;font-style:normal}
.post-date{left:142px;top:43px;font-size:11px;color:#bbb;font-style:italic;font-weight:600}

/* follow */
.follow{left:0;top:1232px;width:1400px;height:124px;background:#e8e8e8}
.follow-title{left:0;top:14px;width:1400px;text-align:center;font-size:28px;color:#222}
.follow-btn{top:60px;width:150px;height:46px;color:#fff;font-family:"Open Sans",sans-serif;font-weight:600;font-size:17px;line-height:46px}
.follow-btn i{position:absolute;left:14px;top:16px;width:12px;height:14px;background:rgba(255,255,255,.9)}
.follow-btn em{position:absolute;left:38px;top:12px;width:1px;height:22px;background:rgba(255,255,255,.35)}
.follow-btn span{position:absolute;left:62px}
.footer-line{left:0;top:1356px;width:1400px;height:6px;background:var(--cyan)}
.footer{left:0;top:1362px;width:1400px;height:54px;background:linear-gradient(#222,#000)}
.footer-links{left:217px;top:21px;font-size:13px;color:#aaa}
.footer-copy{left:926px;top:18px;font-size:13px;color:#aaa}
.under{left:0;top:1416px;width:1400px;height:38px;background:#eee}
</style>
</head>
<body>
<div class="page">

  <header class="abs header">
    <div class="abs brand">
      <div class="brand-mark"></div>
      <div class="brand-name">Havenmark Homes</div>
    </div>
    <div class="abs lang-label cond">Select your language:</div>
    <div class="abs lang-select">English
      <svg width="11" height="7"><path d="M0 0h11L5.5 7z" fill="#fff"/></svg>
    </div>
  </header>

  <nav class="abs nav">
    <div class="abs nav-item active cond" style="left:460px">Home</div>
    <div class="abs nav-item cond" style="left:565px">Properties</div>
    <div class="abs nav-item cond" style="left:676px">News</div>
    <div class="abs nav-item cond" style="left:742px">Blog</div>
    <div class="abs nav-item cond" style="left:811px">Pages</div>
    <div class="abs nav-item cond" style="left:887px">Contact</div>
  </nav>
  <div class="abs social-dot" style="left:1002px" aria-label="Social profile one"></div>
  <div class="abs social-dot" style="left:1053px" aria-label="Social profile two"></div>
  <div class="abs social-dot" style="left:1103px" aria-label="Video channel"></div>

  <section>
    <div class="abs hero-dark"></div>
    <div class="abs hero-blue"></div>
    <div class="abs photo-frame">
      <div class="abs photo" role="img" aria-label="Photo of a modern hotel-style bedroom with a balcony view of the city at dusk"></div>
    </div>

    <form class="abs search">
      <div class="abs search-title cond">Search for homes</div>
      <div class="abs field-label cond" style="top:80px">Location</div>
      <div class="abs select" style="left:112px;top:72px;width:166px">All locations
        <svg width="8" height="5"><path d="M0 0h8L4 5z" fill="#111"/></svg></div>
      <div class="abs field-label cond" style="top:132px">Transaction</div>
      <div class="abs toggle-rent cond">Rent</div>
      <div class="abs toggle-sale cond">Sale</div>
      <div class="abs field-label cond" style="top:207px">No. of rooms</div>
      <div class="abs select" style="left:112px;top:201px;width:76px">Beds
        <svg width="8" height="5"><path d="M0 0h8L4 5z" fill="#111"/></svg></div>
      <div class="abs select" style="left:201px;top:201px;width:77px">Baths
        <svg width="8" height="5"><path d="M0 0h8L4 5z" fill="#111"/></svg></div>
      <div class="abs field-label cond" style="top:248px">Search radius</div>
      <div class="abs slider">
        <div class="abs slider-track"></div>
        <div class="abs knob" style="left:17px"></div>
        <div class="abs knob" style="left:225px"></div>
      </div>
      <div class="abs scale-lbl" style="left:47px">0</div>
      <div class="abs scale-lbl" style="left:93px">2Mil</div>
      <div class="abs scale-lbl" style="left:146px">4Mil</div>
      <div class="abs scale-lbl" style="left:198px">6Mil</div>
      <div class="abs scale-lbl" style="left:251px">8Mil</div>
      <div class="abs find-btn">
        <svg width="12" height="12" style="vertical-align:-1px;margin-right:4px"><circle cx="5" cy="5" r="3.6" fill="none" stroke="#19b4f0" stroke-width="2"/><path d="M7.5 7.5l3.5 3.5" stroke="#19b4f0" stroke-width="2"/></svg>FIND PROPERTIES
      </div>
    </form>

    <div class="abs cat-icon" style="left:237px"><span role="img" aria-label="Illustration of a small house" style="background:linear-gradient(#2b2b2b 50%,#f4f4f4 50%)"></span></div>
    <div class="abs cat-kicker cond" style="left:384px">Properties for</div>
    <div class="abs cat-word" style="left:381px">SALE</div>

    <div class="abs cat-icon" style="left:536px"><span role="img" aria-label="Illustration of a glass office tower" style="background:linear-gradient(#c9dde0,#4fa3a8)"></span></div>
    <div class="abs cat-kicker cond" style="left:685px">Properties for</div>
    <div class="abs cat-word" style="left:684px">RENT</div>

    <div class="abs cat-icon" style="left:832px"><span role="img" aria-label="Illustration of a brick apartment building" style="background:linear-gradient(#e2c9a6,#9b6a3f)"></span></div>
    <div class="abs cat-kicker cond" style="left:987px">Properties for</div>
    <div class="abs cat-word" style="left:979px">LEASE</div>
  </section>

  <div class="abs divider"></div>
  <section class="abs featured">
    <h2 class="abs featured-title cond">Featured properties on sale</h2>
    <svg class="abs" style="left:226px;top:74px" width="20" height="22"><path d="M10 2L2 11l8 9M2 11h18" fill="none" stroke="#111" stroke-width="3.5"/></svg>
    <div class="abs thumb" style="left:264px;background:linear-gradient(#c8c2b8,#7a4a32)" role="img" aria-label="Photo of a furnished bedroom"></div>
    <div class="abs thumb" style="left:408px;background:linear-gradient(#dfe8f0 20%,#9a4a3a 30%,#6a3a2a)" role="img" aria-label="Photo of a red brick townhouse"></div>
    <div class="abs thumb" style="left:553px;background:linear-gradient(#e7ecef 15%,#a2503a 30%,#7a3a2a)" role="img" aria-label="Photo of a brick apartment facade"></div>
    <div class="abs thumb" style="left:694px;background:linear-gradient(#8fb6dd 40%,#8a7564 50%,#6fa23a 65%)" role="img" aria-label="Photo of houses on a green lawn"></div>
    <div class="abs thumb" style="left:839px;background:linear-gradient(#d8d4cc,#3b3530)" role="img" aria-label="Photo of a study room with desks"></div>
    <div class="abs thumb" style="left:984px;background:linear-gradient(#c9dcea 30%,#8d6450 45%,#7aa04a 75%)" role="img" aria-label="Photo of a residential block"></div>
    <svg class="abs" style="left:1131px;top:74px" width="20" height="22"><path d="M10 2l8 9-8 9M18 11H0" fill="none" stroke="#111" stroke-width="3.5"/></svg>
  </section>

  <article>
    <div class="abs blog-kicker">From the Blog:</div>
    <h2 class="abs blog-title cond">Best properties of summer 2013</h2>
    <div class="abs blog-photo"><div role="img" aria-label="Photo of a bright living room with a red sofa"></div></div>
    <div class="abs meta" style="left:477px">Posted by: <b>norvale</b></div>
    <div class="abs blog-date">Tue, Aug 14,12</div>
    <p class="abs blog-body">Lorem ipsum dolor sit amet, consectetuer adipiscing elit, sed diam nonummy nibh euismod tincidunt ut laoreet dolore magna aliquam erat volutpat. Ut wisi enim ad minim veniam, quis nostrud exerci tation ullamcorper suscipit lobortis nisl ut aliquip ex ea commodo consequat.</p>
    <div class="abs more">Continue Reading »</div>
  </article>

  <aside class="abs side">
    <h3 class="abs side-head cond">Latest discussions:</h3>
    <div class="abs post" style="top:74px">
      <svg width="16" height="14"><path d="M8 1C4 1 1 3.3 1 6c0 1.6 1 3 2.6 3.9L3 13l3.6-2.2c.5.1.9.1 1.4.1 4 0 7-2.2 7-4.9S12 1 8 1z" fill="#555"/></svg>
      <div class="abs post-text">Praesent id metus massa, utblandit.</div>
      <div class="abs post-by">by <b>Ada Perrin</b></div>
      <div class="abs post-date">2012-08-14 14:30:16</div>
    </div>
    <div class="abs post" style="top:149px;background:#f4f4f4">
      <svg width="16" height="14"><path d="M8 1C4 1 1 3.3 1 6c0 1.6 1 3 2.6 3.9L3 13l3.6-2.2c.5.1.9.1 1.4.1 4 0 7-2.2 7-4.9S12 1 8 1z" fill="#555"/></svg>
      <div class="abs post-text">Praesent id metus massa, utblandit.</div>
      <div class="abs post-by">by <b>Ada Perrin</b></div>
      <div class="abs post-date">2012-08-14 14:30:16</div>
    </div>
    <div class="abs post" style="top:222px">
      <svg width="16" height="14"><path d="M8 1C4 1 1 3.3 1 6c0 1.6 1 3 2.6 3.9L3 13l3.6-2.2c.5.1.9.1 1.4.1 4 0 7-2.2 7-4.9S12 1 8 1z" fill="#555"/></svg>
      <div class="abs post-text">Praesent id metus massa, utblandit.</div>
      <div class="abs post-by">by <b>Ada Perrin</b></div>
      <div class="abs post-date">2012-08-14 14:30:16</div>
    </div>
  </aside>

  <section class="abs follow">
    <h2 class="abs follow-title cond">Follow us</h2>
    <div class="abs follow-btn" style="left:463px;background:var(--fb)"><i></i><em></em><span>like us!</span></div>
    <div class="abs follow-btn" style="left:630px;background:var(--tw)"><i></i><em></em><span>follow us</span></div>
    <div class="abs follow-btn" style="left:797px;background:var(--li)"><i></i><em></em><span>follow us</span></div>
  </section>

  <div class="abs footer-line"></div>
  <footer class="abs footer">
    <div class="abs footer-links">Villas for Sale • Apartments for Rent • Office Space • Search for one • Latest offers</div>
    <div class="abs footer-copy">Copyright © Havenmark Homes. All Rights Reserved.</div>
  </footer>
  <div class="abs under"></div>

</div>
</body>
</html>
```